Bref créative
Business Stationery
Calvenor Partners
Professional
Belinda Hawthorpe
Managing Director
Ashvale - Brennick - Tolmere
bel@calvenorpartners.com
www.calvenorpartners.com
Quorn Logo
logo vector file

```html
<!DOCTYPE html>
<html lang="en">
<head>
<meta charset="utf-8">
<title>Calvenor Partners – Business Cards</title>
<link href="https://fonts.googleapis.com/css2?family=Open+Sans:wght@400;600;700&display=swap" rel="stylesheet">
<style>
  :root {
    --canvas: #e9ebe6;
    --card: #ffffff;
    --green: #3d9a2f;
    --green-light: #8cc63f;
    --green-dark: #2b7a22;
    --ink: #3b3b3b;
    --ink-soft: #6b6b6b;
    --rule: #d4d4d4;
  }
  * { box-sizing: border-box; margin: 0; padding: 0; }
  html, body {
    width: 1200px; height: 629px; overflow: hidden;
    background: var(--canvas);
    font-family: "Open Sans", Arial, sans-serif;
  }
  .stage {
    width: 1200px; height: 629px;
    display: flex; align-items: center; justify-content: center; gap: 60px;
  }
  .card {
    width: 520px; height: 300px;
    background: var(--card);
    position: relative;
    box-shadow: 0 6px 18px rgba(0,0,0,.12);
    overflow: hidden;
  }
  .card-back {
    display: flex; flex-direction: column; align-items: center; justify-content: center; gap: 18px;
  }
  .brand {
    display: flex; flex-direction: column; align-items: center; gap: 10px;
    color: var(--green); font-weight: 700; white-space: nowrap;
  }
  .brand-dot {
    width: 30px; height: 30px; border-radius: 50%; background: var(--green);
  }
  .card-back .brand-name { font-size: 24px; }
  .back-url {
    color: var(--green); font-size: 11px; letter-spacing: 3px; font-weight: 600;
  }
  .card-front { display: flex; flex-direction: column; }
  .front-body { flex: 1; display: flex; align-items: center; }
  .front-brand {
    width: 50%; display: flex; justify-content: center;
  }
  .front-brand .brand-name { font-size: 21px; }
  .front-details {
    width: 50%; height: 170px;
    border-left: 1px solid var(--rule);
    padding-left: 18px;
    display: flex; flex-direction: column; justify-content: center;
  }
  .person-name { font-size: 15px; font-weight: 700; color: var(--ink); white-space: nowrap; }
  .person-title { font-size: 11px; color: var(--ink-soft); margin-bottom: 12px; }
  .contact-list { list-style: none; display: flex; flex-direction: column; gap: 5px; }
  .contact-item { display: flex; align-items: center; gap: 8px; font-size: 11px; color: var(--ink); white-space: nowrap; }
  .contact-icon { width: 13px; height: 13px; flex: none; }
  .front-band {
    height: 64px;
    background: linear-gradient(180deg, var(--green-light), var(--green) 55%, var(--green-dark));
    display: flex; align-items: center; justify-content: center;
  }
  .band-url { color: #fff; font-size: 12px; letter-spacing: 3px; font-weight: 600; }
</style>
</head>
<body>
<main class="stage">
  <section class="card card-back">
    <div class="brand">
      <span class="brand-dot"></span>
      <span class="brand-name">Calvenor Partners</span>
    </div>
    <p class="back-url">www.calvenorpartners.com</p>
  </section>

  <section class="card card-front">
    <div class="front-body">
      <div class="front-brand">
        <div class="brand">
          <span class="brand-dot"></span>
          <span class="brand-name">Calvenor Partners</span>
        </div>
      </div>
      <div class="front-details">
        <p class="person-name">Belinda Hawthorpe</p>
        <p class="person-title">Managing Director</p>
        <ul class="contact-list">
          <li class="contact-item">
            <svg class="contact-icon" viewBox="0 0 14 14"><circle cx="7" cy="7" r="7" fill="var(--green)"/><path d="M7 3.2a2.4 2.4 0 0 0-2.4 2.4C4.6 7.5 7 10.8 7 10.8s2.4-3.3 2.4-5.2A2.4 2.4 0 0 0 7 3.2z" fill="#fff"/></svg>
            Ashvale - Brennick - Tolmere
          </li>
          <li class="contact-item">
            <svg class="contact-icon" viewBox="0 0 14 14"><circle cx="7" cy="7" r="7" fill="var(--green)"/><path d="M4.5 3.5l1.5 0 .7 1.8-.9.7a5 5 0 0 0 2.2 2.2l.7-.9 1.8.7v1.5c-3.5.3-6.3-2.5-6-6z" fill="#fff"/></svg>
            +000 1 555 0198
          </li>
          <li class="contact-item">
            <svg class="contact-icon" viewBox="0 0 14 14"><circle cx="7" cy="7" r="7" fill="var(--green)"/><rect x="3.5" y="4.5" width="7" height="5" fill="#fff"/><path d="M3.5 4.5L7 7.3l3.5-2.8" stroke="var(--green)" stroke-width=".8" fill="none"/></svg>
            bel@calvenorpartners.com
          </li>
          <li class="contact-item">
            <svg class="contact-icon" viewBox="0 0 14 14"><circle cx="7" cy="7" r="7" fill="var(--green)"/><circle cx="7" cy="7" r="3.3" stroke="#fff" stroke-width=".9" fill="none"/><path d="M3.7 7h6.6M7 3.7v6.6" stroke="#fff" stroke-width=".8"/></svg>
            www.calvenorpartners.com
          </li>
        </ul>
      </div>
    </div>
    <div class="front-band">
      <p class="band-url">www.calvenorpartners.com</p>
    </div>
  </section>
</main>
</body>
</html>
```